Company letter head

Hello,
We are a global logistics company requiring a letterhead design for all our company documentation.
Company Name: Clearly display the full name of your company at the top of the letterhead.
Logo: Include your company logo for brand recognition.
Contact Information: This includes your company's address, phone number, email address, and website URL.
Target Market(s)
Clients/customers
Industry/Entity Type
Logistics
Font styles to use
Sans Serif
Requirements
Must have
- Company name and logo
Nice to have
- borders, header/footers

```html
<!DOCTYPE html>
<html lang="en">
<head>
<meta charset="utf-8">
<title>Meridian Freight Lines — Letterhead</title>
<link href="https://fonts.googleapis.com/css2?family=Arimo:wght@400;700&family=Mulish:wght@600;700&display=swap" rel="stylesheet">
<style>
  :root {
    --backdrop: #d2d2d2;
    --paper: #ffffff;
    --header-dark: #414141;
    --brand-red: #d51f26;
    --ink: #555555;
    --ink-strong: #4a4a4a;
    --header-text: #f2f2f2;
    --divider: #9a9a9a;
  }
  * { margin: 0; padding: 0; box-sizing: border-box; }
  html, body {
    width: 1200px;
    height: 1055px;
    overflow: hidden;
    background: var(--backdrop);
  }
  .letterhead {
    position: absolute;
    left: 281px;
    top: 77px;
    width: 638px;
    height: 901px;
    background: var(--paper);
    overflow: hidden;
    font-family: "Arimo", Arial, sans-serif;
  }
  .masthead {
    position: absolute;
    left: 0; top: 0;
    width: 100%;
    height: 105px;
    background: var(--header-dark);
  }
  .masthead-rule {
    position: absolute;
    left: 0; top: 110px;
    width: 100%;
    height: 4px;
    background: var(--brand-red);
  }
  .brand {
    position: absolute;
    left: 43px;
    top: 44px;
    display: flex;
    align-items: center;
    gap: 8px;
  }
  .brand-dot {
    width: 16px;
    height: 16px;
    border-radius: 50%;
    background: var(--brand-red);
  }
  .brand-name {
    color: var(--header-text);
    font-family: "Arimo", Arial, sans-serif;
    font-weight: 700;
    font-size: 15px;
    letter-spacing: 0.2px;
  }
  .address {
    position: absolute;
    right: 195px;
    top: 51px;
    text-align: right;
    color: var(--header-text);
    font-size: 11px;
    line-height: 13px;
  }
  .contact-divider {
    position: absolute;
    left: 454px;
    top: 47px;
    width: 1px;
    height: 35px;
    background: var(--divider);
  }
  .contacts {
    position: absolute;
    left: 466px;
    top: 44px;
    list-style: none;
    color: var(--header-text);
    font-size: 11px;
    line-height: 13px;
  }
  .contacts li {
    display: flex;
    align-items: center;
    gap: 6px;
  }
  .contacts svg { width: 8px; height: 8px; flex: none; }
  .letter {
    position: absolute;
    left: 56px;
    top: 276px;
    width: 524px;
    color: var(--ink);
  }
  .salutation {
    font-family: "Mulish", "Century Gothic", sans-serif;
    font-weight: 700;
    font-size: 14.5px;
    color: var(--ink-strong);
    margin-left: 2px;
    margin-bottom: 22px;
  }
  .letter p {
    font-size: 10.3px;
    line-height: 13.1px;
    margin-bottom: 11.5px;
  }
  .closing {
    font-family: "Mulish", "Century Gothic", sans-serif;
    font-weight: 700;
    font-size: 8.5px;
    color: var(--ink-strong);
    margin-top: 20px;
    margin-left: 1px;
  }
  .signature {
    width: 105px;
    height: 30px;
    margin-top: 26px;
    margin-left: 2px;
    background: linear-gradient(90deg, #e6e6e6, #f1f1f1);
  }
  .footer-band {
    position: absolute;
    left: 0; bottom: 0;
    width: 100%;
    height: 14px;
    background: var(--brand-red);
  }
</style>
</head>
<body>
  <div class="letterhead">
    <header class="masthead">
      <div class="brand">
        <span class="brand-dot"></span>
        <span class="brand-name">Meridian Freight Lines</span>
      </div>
      <div class="address">Your address, city<br>state, ZIP 0000</div>
      <div class="contact-divider"></div>
      <ul class="contacts">
        <li>
          <svg viewBox="0 0 10 10" aria-hidden="true"><path d="M2 1 L3.6 1 L4.3 3 L3.3 3.8 Q4.3 5.8 6.2 6.7 L7 5.7 L9 6.4 L9 8 Q9 9 8 9 Q1 8.5 1 2 Q1 1 2 1 Z" fill="#d51f26"/></svg>
          123-456-2100
        </li>
        <li>
          <svg viewBox="0 0 10 10" aria-hidden="true"><rect x="0.5" y="2" width="9" height="6" fill="#d51f26"/><path d="M0.5 2 L5 5.5 L9.5 2" fill="none" stroke="#414141" stroke-width="0.9"/></svg>
          youremail@mailbox.com
        </li>
        <li>
          <svg viewBox="0 0 10 10" aria-hidden="true"><circle cx="5" cy="5" r="4.3" fill="#d51f26"/><path d="M0.8 5 H9.2 M5 0.7 Q2.5 5 5 9.3 M5 0.7 Q7.5 5 5 9.3" fill="none" stroke="#414141" stroke-width="0.7"/></svg>
          www.yourwebsite.com
        </li>
      </ul>
    </header>
    <div class="masthead-rule"></div>

    <main class="letter">
      <h1 class="salutation">Dear Mr. Harlow,</h1>
      <p>Lorem ipsum dolor sit amet, consectetuer adipiscing elit, sed diam nonmmy nibh euismod tincidunt ut laor eet dolore magna aliquam erat volutpat. Ut wisi enim ad minim veniam, quis nostrud exerci tationmcorper suscipit lobortis nisl ut aliquip ex ea commodo consequat. Duis autem vel eum iriure dolor in hendrerit in vulputate velit esse molestie consequat, vel illum dolore eu feugiat</p>
      <p>Rorem ipsum dolor sit amet, consectetuer adipiscing elit, sed diam nonmmy nibh euismod tincidunt ut laor eet dolore magna aliquam erat volutpat. Ut wisi enim ad minim veniam, quis nostrud exerci tationmcorper suscipit lobortis nisl ut aliquip ex ea commodo consequat. Duis autem vel eum iriure dolor in hendrerit in vulputate velit esse molest</p>
      <p>Dorem ipsum dolor sit amet, consectetuer adipiscing elit, sed diam nonmmy nibh euismod tincidunt ut laor eet dolore magna aliquam erat volutpat. Ut wisi enim ad minim veniam, quis nostrud exerci tationmcorper suscipit lobortis nisl ut aliquip ex ea commodo consequat. Duis autem vel eum iriure dolor in hendrerit in suscipit lobortis nisl ut aliquip ex ea commodo consequat. Duis autem vel eum iriure dolor in hendrerit in vulputate velit esse molestie consequat, vel illum</p>
      <p>Sorem ipsum dolor sit amet, consectetuer adipiscing elit, sed diam nonmmy nibh euismod tincidunt ut laor eet dolore magna aliquam erat volutpat. Ut wisi enim ad minim veniam, quis nostrud exerci tationmcorper suscipit lobortis nisl ut aliquip ex ea commodo consequat. Duis autem vel eum iriure dolor in</p>
      <div class="closing">Sincerely,</div>
      <div class="signature" role="img" aria-label="Handwritten signature of the sender"></div>
    </main>

    <footer class="footer-band"></footer>
  </div>
</body>
</html>
```